Business Card Design

I am an independent consultant to the telecommunications industry. I specialize in helping equipment manufacturers of high end fiber optic telecommunications products market and sell their products to end users such as qw&z, Palomex, Brisk Harlow Cable, Quorva 8, Dovix, etc. I conduct this activity on a global or worldwide basis. I need a professional looking card that contains a high-tech telecommunications related logo. I am thinking of something along the lines of two telephone poles separated by a bright narrow beam of light (as opposed to traditional wire) and perhaps spanning a spherical globe (world).
Target Market(s)
Engineers, Executives and Purchasing Agents for Large Gazette 700 companies
Industry/Entity Type
Telecommunications
Contact Information for Business Card
Gil Parsons, President, Oakmere Technology Partners, LLC, 4826-Bramwell Drive, Pilot Point, TX 75492-1847, 469-555-0148

```html
<!DOCTYPE html>
<html lang="en">
<head>
<meta charset="utf-8">
<title>Gil Parsons – Business Card</title>
<link rel="stylesheet" href="https://fonts.googleapis.com/css2?family=Arimo:ital,wght@0,400;0,700;1,400&display=swap">
<style>
  :root {
    --card-blue: #0191de;
    --panel-blue: #74c3ef;
    --text-white: #ffffff;
    --mark-teal: #3f8f94;
  }
  html, body {
    margin: 0;
    padding: 0;
    overflow: hidden;
    background: #ffffff;
  }
  .card {
    position: relative;
    width: 1200px;
    height: 705px;
    background: var(--card-blue);
    overflow: hidden;
    font-family: "Arimo", Arial, sans-serif;
    color: var(--text-white);
  }
  .name-panel {
    position: absolute;
    left: 0;
    top: 169px;
    width: 705px;
    height: 228px;
    background: var(--panel-blue);
  }
  .person-name {
    position: absolute;
    left: 0;
    width: 710px;
    top: 245px;
    margin: 0;
    text-align: center;
    font-size: 78px;
    font-weight: 700;
    line-height: 1;
  }
  .person-title {
    position: absolute;
    left: 0;
    width: 710px;
    top: 334px;
    margin: 0;
    text-align: center;
    font-size: 44px;
    font-style: italic;
    font-weight: 400;
    line-height: 1;
  }
  .brand-mark {
    position: absolute;
    left: 830px;
    top: 108px;
    width: 300px;
    text-align: center;
  }
  .brand-mark svg {
    display: block;
    margin: 0 auto;
  }
  .brand-mark .brand-name {
    margin-top: 16px;
    font-size: 40px;
    font-weight: 700;
    color: var(--text-white);
    line-height: 1;
  }
  .company-block {
    position: absolute;
    left: 260px;
    width: 802px;
    top: 490px;
    margin: 0;
    text-align: center;
    font-size: 41px;
    font-weight: 700;
    line-height: 57px;
    font-style: normal;
  }
</style>
</head>
<body>
  <div class="card">
    <div class="name-panel"></div>
    <h1 class="person-name">Gil Parsons</h1>
    <p class="person-title">President</p>

    <div class="brand-mark">
      <svg width="230" height="230" viewBox="0 0 230 230" aria-hidden="true">
        <circle cx="115" cy="115" r="112" fill="var(--mark-teal)"/>
      </svg>
      <div class="brand-name">Oakmere</div>
    </div>

    <address class="company-block">
      Oakmere Technology Partners, LLC<br>
      4826-Bramwell Drive, Larkspur Bend<br>
      TX 75492-1847, 469-555-0148
    </address>
  </div>
</body>
</html>
```